依頼詳細
詳細は別紙参照下さい。
記載項目
詳細は別紙参照下さい。
希望イメージ
シンプル 複雑
単色 カラフル
暗い 明るい
日常 高級
遊び心 厳粛
未来的 伝統的
女性的 男性的
希望する色
納品ファイル
• イラストレーター形式 (.ai)
補足説明
■ 選んだ理由

有名ブランド森光のルミナF業務用ミニボトルが廃盤となり後継商品とするのにこだわりの成分で製造した商品である事がとても分かり易いデザインで、未だ認知度の低い製品でもストレートに利用客様に伝わるデザインである事や、お子様セットに使用してもママさんが見て我が子に使用するのに安心出来るデザインである事から決定の運びとなりました。

■ 提案者全員のお礼・コメント

この度は90案以上のデザインのご提案を頂く事となり皆さまに深くお礼申し上げます。ご提案のレベルも大変高く、多くの候補が残り我が社の協議で決定となるまで絞り込むのに大変熱く論じ合う事となりました。おかげさまで社員一同納得をして最善のものを選択出来たと思っております。今後も当サイトにてお願いする事が出てくるかと存じますが、機会がございましたら何卒宜しくお願い申し上げます。

```html
<!DOCTYPE html>
<html lang="ja">
<head>
<meta charset="utf-8">
<title>Botanical Body Soap – Sachet</title>
<link href="https://fonts.googleapis.com/css2?family=Great+Vibes&family=Marcellus&family=Noto+Sans+JP:wght@400;500&family=Jost:wght@400;500&display=swap" rel="stylesheet">
<style>
  :root {
    --page-bg: #ffffff;
    --green-deep: #3c6a45;
    --green-mid: #4f7f52;
    --green-light: #6f9c63;
    --ink-light: #f3f6ef;
    --swatch-light: #8cc171;
    --swatch-deep: #3e6f4d;
    --swatch-white: #ffffff;
    --swatch-grey: #646464;
    --swatch-edge: #c9c9c9;
  }
  * { margin: 0; padding: 0; box-sizing: border-box; }
  html, body {
    width: 706px; height: 1200px; overflow: hidden;
    background: var(--page-bg);
  }
  .canvas { position: relative; width: 706px; height: 1200px; }

  .sachet {
    position: absolute; left: 177px; top: 136px;
    width: 364px; height: 864px;
    background:
      linear-gradient(100deg, rgba(255,255,255,0) 30%, rgba(255,255,255,0.12) 48%, rgba(255,255,255,0) 62%),
      linear-gradient(180deg, var(--green-light) 0%, var(--green-mid) 35%, var(--green-deep) 70%, var(--green-mid) 100%);
    box-shadow: 0 4px 10px rgba(0,0,0,0.12);
    overflow: hidden;
    color: var(--ink-light);
  }
  .sachet__crimp {
    position: absolute; left: 0; right: 0; height: 30px;
    background: repeating-linear-gradient(90deg, rgba(255,255,255,0.10) 0 2px, rgba(0,0,0,0.06) 2px 5px);
  }
  .sachet__crimp--top { top: 0; }
  .sachet__crimp--bottom { bottom: 0; }
  .sachet__side {
    position: absolute; top: 30px; bottom: 30px; width: 18px;
    background: repeating-linear-gradient(0deg, rgba(255,255,255,0.08) 0 2px, rgba(0,0,0,0.05) 2px 5px);
  }
  .sachet__side--left { left: 0; }
  .sachet__side--right { right: 0; }

  .foliage {
    position: absolute; left: 0; top: 0; width: 364px; height: 260px;
    background: linear-gradient(180deg, rgba(160,196,140,0.35), rgba(160,196,140,0));
  }

  .badge {
    position: absolute; left: 212px; top: 150px; width: 132px; height: 132px;
  }

  .title { position: absolute; left: 80px; top: 286px; }
  .title__script {
    font-family: "Great Vibes", cursive;
    font-size: 54px; line-height: 1; font-weight: 400;
  }
  .title__sub {
    margin-top: 4px;
    font-family: "Jost", sans-serif;
    font-size: 24px; letter-spacing: 3px; font-weight: 400;
  }
  .title__rule {
    margin-top: 10px; width: 36px; height: 1.5px; background: var(--ink-light);
  }
  .title__claim {
    margin-top: 12px;
    font-family: "Noto Sans JP", sans-serif;
    font-size: 19px; line-height: 1.45;
  }

  .lead {
    position: absolute; left: 80px; top: 634px;
    font-family: "Noto Sans JP", sans-serif;
    font-size: 21px; line-height: 1.4;
  }
  .product-name {
    position: absolute; left: 78px; top: 706px;
    font-family: "Marcellus", serif;
    font-size: 64px; font-weight: 400; letter-spacing: 4px; line-height: 1;
  }

  .palette {
    position: absolute; top: 1136px; left: 167px;
    display: flex; gap: 44px;
  }
  .palette__chip {
    width: 42px; height: 42px; border-radius: 50%;
  }
  .palette__chip--light { background: var(--swatch-light); }
  .palette__chip--deep { background: var(--swatch-deep); }
  .palette__chip--white { background: var(--swatch-white); border: 1.5px solid var(--swatch-edge); }
  .palette__chip--grey { background: var(--swatch-grey); }
</style>
</head>
<body>
<main class="canvas">
  <section class="sachet">
    <div class="foliage" role="img" aria-label="Faint line drawing of leafy botanical branches"></div>
    <div class="sachet__crimp sachet__crimp--top"></div>
    <div class="sachet__crimp sachet__crimp--bottom"></div>
    <div class="sachet__side sachet__side--left"></div>
    <div class="sachet__side sachet__side--right"></div>

    <svg class="badge" viewBox="0 0 132 132" aria-label="Plant-derived ingredients">
      <defs>
        <path id="badge-ring" d="M66,66 m-48,0 a48,48 0 1,1 96,0 a48,48 0 1,1 -96,0"/>
      </defs>
      <text font-family="Jost, sans-serif" font-size="11" letter-spacing="1.6" fill="#f3f6ef">
        <textPath href="#badge-ring" startOffset="2%">PLANT-DERIVED · INGREDIENTS ·</textPath>
      </text>
      <circle cx="66" cy="66" r="15" fill="none" stroke="#f3f6ef" stroke-width="1.4"/>
    </svg>

    <div class="title">
      <div class="title__script">Botanical</div>
      <div class="title__sub">BODY SOAP</div>
      <div class="title__rule"></div>
      <p class="title__claim">植物由来成分<br>100%</p>
    </div>

    <p class="lead">お肌に優しい<br>ボディソープ</p>
    <h1 class="product-name">ALVE</h1>
  </section>

  <div class="palette">
    <span class="palette__chip palette__chip--light"></span>
    <span class="palette__chip palette__chip--deep"></span>
    <span class="palette__chip palette__chip--white"></span>
    <span class="palette__chip palette__chip--grey"></span>
  </div>
</main>
</body>
</html>
```